Charitable and Benefit Event Auctioneer and Emcee

My name is Lem
People know me as Lem The Auctioneer
My email is lemtheauctioneer@...
Include Phone number
This is a very unique and distinct type of Auctioneering that focuses on high profile charitable events including black tie galas, fundraisers and golf tournaments...
Clients include hospitals, schools, service agencies, corporations, foundations
Event consultation is also offered
Graduate of The Brackmoor Valley College of Auctioneering
in the Fundraising Auction business since 1998

Project Deadline Extended
Reason: I have been too busy to give time to appropriate time to the designs submitted and I'm still having learning challenges with the artquarry website.

Target Market(s)

Very high profile nonprofit organizations hosting gala events raising millions of dollars.

Industry/Entity Type

Events

Font styles to use
Sans Serif

Colors

Designer to choose colors to be used in the design.

Requirements
Must have
• Classy, eye catching, unique.

```html
<!DOCTYPE html>
<html lang="en">
<head>
<meta charset="utf-8">
<title>Lem The Auctioneer — Business Card</title>
<link rel="stylesheet" href="https://fonts.googleapis.com/css2?family=Exo+2:wght@300;400;500&display=swap">
<style>
  :root {
    --backdrop: #c9c9cc;
    --card-front: #4e1416;
    --card-back: #5c1114;
    --gold: #f0a81c;
    --ivory: #f4efe9;
    --rule: rgba(240, 168, 28, 0.45);
  }
  * { margin: 0; padding: 0; box-sizing: border-box; }
  html, body {
    width: 1200px;
    height: 900px;
    overflow: hidden;
  }
  body {
    background: var(--backdrop);
    font-family: "Exo 2", sans-serif;
    position: relative;
  }
  .card {
    position: absolute;
    left: 320px;
    width: 560px;
    height: 320px;
    border-radius: 28px;
    box-shadow: 0 6px 18px rgba(0, 0, 0, 0.18);
    display: flex;
    flex-direction: column;
    align-items: center;
    justify-content: center;
    padding: 0 48px;
  }
  .card-front {
    top: 100px;
    background: var(--card-front);
  }
  .card-back {
    top: 480px;
    background: var(--card-back);
  }
  .brand-name {
    display: flex;
    align-items: center;
    gap: 14px;
    color: var(--gold);
    font-weight: 400;
    font-size: 27px;
    letter-spacing: 0.1em;
    text-transform: uppercase;
    white-space: nowrap;
  }
  .brand-square {
    flex: none;
    width: 24px;
    height: 24px;
    border: 2px solid var(--gold);
  }
  .contact-phone {
    color: var(--gold);
    font-size: 40px;
    font-weight: 400;
    letter-spacing: 0.01em;
    padding: 0 24px 10px;
    border-bottom: 1px solid var(--rule);
  }
  .contact-email {
    color: var(--gold);
    font-size: 21px;
    font-weight: 400;
    margin-top: 12px;
  }
  .back-name {
    display: flex;
    align-items: center;
    gap: 12px;
    margin-top: 34px;
    color: var(--ivory);
    font-size: 28px;
    font-weight: 400;
    letter-spacing: 0.18em;
    text-transform: uppercase;
  }
  .back-name .brand-square {
    width: 22px;
    height: 22px;
    border-color: var(--ivory);
  }
</style>
</head>
<body>
  <section class="card card-front" aria-label="Card front">
    <div class="brand-name">
      <span class="brand-square"></span>
      <span>Lem The Auctioneer</span>
    </div>
  </section>

  <section class="card card-back" aria-label="Card back">
    <div class="contact-phone">555.214.0397</div>
    <div class="contact-email">lemtheauctioneer@northmail.ca</div>
    <div class="back-name">
      <span class="brand-square"></span>
      <span>Lem</span>
    </div>
  </section>
</body>
</html>
```